Personal sales brochure for client marketing

I am looking for a brochure in the style of a sales menu to sit in front of clients with. I want 5 different colored columns where clients will choose the right package for them.
Eg.
Package 1 called Book-keeping is a basic package
Package 2 called Insight includes the above but also extra services
Package 3 called Compliance an add on for the above packages
Package 4 Called Professional another add on to the above services
Package 5 called payroll another add on to the above.

I want to sit in front of my clients and discuss the services we provide and allow them to choose from this list and tick the boxes of what they would like. I attach a simple spread sheet as well for guideline.

Target Market(s)

business owners requiring accounting support and advice

Industry/Entity Type

Accounting

Font styles to use
Serif
Sans Serif

Requirements
Must have
• Simple, clear, concise with clear product descriptions in colored boxes that highlight clearly the different options. Must have Logo and contact details. This document need to be our key sales and marketing tool so will need to introduce the business clearly and in a professional manner.
• enquiries@brantwellpartners.gg
• 01481 439216
Nice to have
• The design needs to be printable on A1 A3 A4 A5
Should not have
• Pictures and patterns

```html
<!DOCTYPE html>
<html lang="en">
<head>
<meta charset="utf-8">
<title>Brantwell Partners – Services</title>
<link rel="stylesheet" href="https://fonts.googleapis.com/css2?family=Crimson+Text:ital,wght@0,400;1,400&family=Open+Sans:wght@400;600&display=swap">
<style>
  :root {
    --page-top: #f7f7f7;
    --page-bottom: #ececec;
    --band: #dadada;
    --ink: #555658;
    --logo-grey: #6d6e71;
    --logo-green: #3a9a58;
    --payroll: #ef7f33;
    --payroll-dark: #c4611e;
    --bookkeeping: #a33139;
    --bookkeeping-dark: #7c2229;
    --insight: #2ea84f;
    --insight-dark: #1f7e3a;
    --compliance: #e83c39;
    --compliance-dark: #b82a28;
    --professional: #22a3bd;
    --professional-dark: #177b8f;
    --contact-bg: #58595b;
    --white: #ffffff;
  }
  html, body { margin: 0; padding: 0; overflow: hidden; }
  body { width: 1200px; height: 848px; }
  .sheet {
    position: relative;
    width: 1200px; height: 848px; overflow: hidden;
    background: linear-gradient(180deg, var(--page-top), var(--page-bottom));
    font-family: "Open Sans", Arial, sans-serif;
    color: var(--ink);
  }
  .shapes { position: absolute; left: 0; top: 0; }
  .brand { position: absolute; left: 56px; top: 62px; width: 320px; white-space: nowrap; }
  .brand-name {
    font-family: "Crimson Text", Georgia, serif;
    font-size: 25px; line-height: 1; letter-spacing: 0.5px;
    color: var(--logo-grey); margin: 0; font-weight: 400;
  }
  .brand-tagline {
    margin: 14px 0 0; font-size: 10.5px; letter-spacing: 2.2px;
    color: var(--logo-green); text-transform: uppercase;
  }
  .intro {
    position: absolute; left: 393px; top: 52px; width: 790px; margin: 0;
    font-family: "Crimson Text", Georgia, serif; font-style: italic;
    font-size: 21px; line-height: 34px; color: var(--ink);
  }
  .package {
    position: absolute; top: 166px; width: 186px; height: 506px;
    color: var(--white);
  }
  .package-title {
    margin: 52px 20px 0; padding-bottom: 10px;
    border-bottom: 1px solid rgba(255,255,255,0.85);
    font-family: "Crimson Text", Georgia, serif; font-style: italic; font-weight: 400;
    font-size: 20px; text-align: center; letter-spacing: 0.5px;
  }
  .package-items { list-style: none; margin: 22px 0 0; padding: 0 22px 0 25px; }
  .package-items li {
    font-size: 12.8px; line-height: 16.6px; margin-bottom: 19px;
    overflow-wrap: anywhere;
  }
  .package-note {
    position: absolute; left: 25px; right: 14px; top: 436px; margin: 0;
    font-size: 12.8px; line-height: 17px; font-style: italic;
  }
  .catchup {
    position: absolute; left: 54px; top: 752px; margin: 0; width: 780px;
    font-family: "Crimson Text", Georgia, serif; font-style: italic;
    font-size: 15px; line-height: 27px; color: var(--ink);
  }
  .contact {
    position: absolute; left: 850px; top: 740px; width: 350px; height: 74px;
    background: var(--contact-bg); color: var(--white);
    font-weight: 600; font-size: 16px; font-style: normal;
    padding: 8px 0 0 22px; box-sizing: border-box; white-space: nowrap;
  }
  .contact-line { display: flex; align-items: center; height: 29px; }
  .contact-line svg { width: 16px; height: 16px; margin-right: 10px; flex: none; }
</style>
</head>
<body>
<main class="sheet">
  <svg class="shapes" width="1200" height="848" viewBox="0 0 1200 848" aria-hidden="true">
    <rect class="band" x="0" y="204" width="1200" height="504" fill="var(--band)"/>
    <g class="ribbon">
      <polygon points="40,198 54,166 54,198" fill="var(--payroll-dark)"/>
      <polygon points="54,166 240,166 240,672 147,726 54,672" fill="var(--payroll)"/>
    </g>
    <g class="ribbon">
      <polygon points="268,198 282,166 282,198" fill="var(--bookkeeping-dark)"/>
      <polygon points="282,166 468,166 468,672 375,726 282,672" fill="var(--bookkeeping)"/>
    </g>
    <g class="ribbon">
      <polygon points="496,198 510,166 510,198" fill="var(--insight-dark)"/>
      <polygon points="510,166 696,166 696,672 603,726 510,672" fill="var(--insight)"/>
    </g>
    <g class="ribbon">
      <polygon points="724,198 738,166 738,198" fill="var(--compliance-dark)"/>
      <polygon points="738,166 924,166 924,672 831,726 738,672" fill="var(--compliance)"/>
    </g>
    <g class="ribbon">
      <polygon points="952,198 966,166 966,198" fill="var(--professional-dark)"/>
      <polygon points="966,166 1152,166 1152,672 1059,726 966,672" fill="var(--professional)"/>
    </g>
  </svg>

  <header class="brand">
    <p class="brand-name">BRANTWELL PARTNERS</p>
    <p class="brand-tagline">Accounting &amp; Business Solutions</p>
  </header>

  <p class="intro">Every business is different and when we understand your needs we can provide just<br>the services you require for an agreed fee. Our services fall into the following categories:</p>

  <section class="package package-payroll" style="left:54px">
    <h2 class="package-title">PAYROLL</h2>
    <ul class="package-items">
      <li>Weekly/monthly</li>
      <li>ETI Returns</li>
      <li>UK/Channel Island</li>
    </ul>
  </section>

  <section class="package package-bookkeeping" style="left:282px">
    <h2 class="package-title">BOOK-KEEPING</h2>
    <ul class="package-items">
      <li>Monthly/Quarterly/Annually its your choice</li>
      <li>Invoices entered and bank accounts reconciled</li>
      <li>Purchase and sales ledgers reconciled</li>
    </ul>
    <p class="package-note">All software is included. Unlimited support and assistance.</p>
  </section>

  <section class="package package-insight" style="left:510px">
    <h2 class="package-title">INSIGHT</h2>
    <ul class="package-items">
      <li>Monthly/Quarterly/Annually its your choice</li>
      <li>Book-keeping + :</li>
      <li>Accounting adjustments to give a true reflection of your profit/loss to date</li>
      <li>Management Accounts</li>
      <li>Regular meeting to discuss business performance and possible areas for improvement</li>
    </ul>
    <p class="package-note">All software is included. Unlimited support and assistance.</p>
  </section>

  <section class="package package-compliance" style="left:738px">
    <h2 class="package-title">COMPLIANCE</h2>
    <ul class="package-items">
      <li>What every business must do:</li>
      <li>Financial statements prepared</li>
      <li>Income tax computation</li>
      <li>Personal tax returns</li>
    </ul>
    <p class="package-note">All software is included. Unlimited support and assistance.</p>
  </section>

  <section class="package package-professional" style="left:966px">
    <h2 class="package-title">PROFESSIONAL</h2>
    <ul class="package-items">
      <li>Bespoke solutions for your business</li>
      <li>Business planning</li>
      <li>Cash flow planning and forecasting</li>
      <li>Specialist tax planning</li>
      <li>Business turnaround</li>
    </ul>
    <p class="package-note">All software is included. Unlimited support and assistance.</p>
  </section>

  <p class="catchup">Many clients have a need for a "catch-up" project to get their books and accounts up to date.<br>We will agree with you a plan to complete the project at the outset and agree a fixed price.&nbsp; Interest free credit is</p>

  <address class="contact">
    <div class="contact-line">
      <svg viewBox="0 0 18 18" aria-hidden="true"><rect x="1" y="4" width="16" height="11" fill="var(--white)"/><polyline points="1,4 9,10.5 17,4" fill="none" stroke="var(--contact-bg)" stroke-width="1.6"/></svg>
      enquiries@brantwellpartners.gg
    </div>
    <div class="contact-line">
      <svg viewBox="0 0 18 18" aria-hidden="true"><path d="M4.2 1.5l3 3.4-1.8 2.1c.9 2 2.5 3.7 4.6 4.6l2.1-1.8 3.4 3-1.6 2.7C8.4 15.3 2.7 9.6 1.5 3.1z" fill="var(--white)"/></svg>
      01481 439216
    </div>
  </address>
</main>
</body>
</html>
```